Math Tuition center needs a fresh website with LMS

I'm intending to buy a LMS theme for my wordpress site. But I need someone to help me design a few posters for the slider and set up the entire site for me. The LMS theme I'm eyeing has everything I need. But I don't have the time to figure things out.
I'm looking at either:
http://themes.brightpanel.com/smartlesson/
or
http://gallerydeck.org/vantor/
My current site is online at www.tallywise.com
I also need you to help me clear up the files I don't need on the server. So basically I need someone to design the new site for me, the LMS theme should make things easier but I'll need some customizations. I also need a webmaster who can help me set up the entire site so I don't have to turn on the widget or mess around with the theme.
Another thing, I have SEO done onsite so I can't change the contents, the meta-tags and such.
Industry/Entity Type
Online
Look and feel
Each slider illustrates characteristics of the customer's brand and the style your logo design should communicate.

```html
<!DOCTYPE html>
<html lang="en">
<head>
<meta charset="utf-8">
<title>tallywise – Math Tuition</title>
<link rel="stylesheet" href="https://fonts.googleapis.com/css2?family=Raleway:wght@400;500;600;700;800&family=Open+Sans:wght@400;600;700&display=swap">
<style>
:root{
  --green:#8dc63f;
  --teal:#6fd0c4;
  --ink:#333;
  --body:#888;
  --muted:#aaa;
  --line:#e6e6e6;
  --band:#f3f3f3;
  --dark:#2b2b2b;
  --darker:#1f1f1f;
  --hero:#3a3a3a;
}
*{box-sizing:border-box;margin:0;padding:0}
html,body{width:1200px;height:3902px;overflow:hidden}
body{font-family:"Open Sans",Arial,sans-serif;color:var(--body);background:#fff;font-size:13px;line-height:1.6}
h1,h2,h3,h4,h5,.nav,.btn{font-family:"Raleway",Arial,sans-serif}
.wrap{width:1038px;margin:0 auto;position:relative}
.btn{display:inline-block;color:#fff;font-size:11px;font-weight:700;letter-spacing:1px;text-transform:uppercase;padding:12px 22px;border-radius:2px}
.btn-teal{background:var(--teal)}
.btn-dark{background:#4a4a4a}

/* header */
.site-header{height:98px;border-bottom:1px solid var(--line)}
.site-header .wrap{display:flex;align-items:center;justify-content:space-between;height:98px}
.brand{display:flex;align-items:center;gap:10px;font-family:"Raleway",sans-serif;font-size:30px;font-weight:700;color:var(--green)}
.brand-dot{width:18px;height:18px;border-radius:50%;background:var(--green)}
.nav{display:flex;font-size:12px;font-weight:600;letter-spacing:1px;color:#666}
.nav a{padding:0 22px;border-left:1px solid var(--line)}
.nav a:first-child{border-left:0;color:var(--ink);font-weight:700}

/* hero */
.hero{height:455px;position:relative;background:linear-gradient(90deg,#8a8a8a 0%,#5e5e5e 30%,var(--hero) 60%,#2e2e2e 100%);overflow:hidden}
.hero-photo{position:absolute;left:0;top:0;width:560px;height:455px;background:radial-gradient(ellipse at 40% 55%,#c07a92 0%,#8c6a72 35%,rgba(90,90,90,0) 75%)}
.hero-copy{position:absolute;right:88px;top:118px;width:760px;text-align:right;color:#fff}
.hero-copy h1{font-size:56px;font-weight:800;letter-spacing:1.5px;line-height:1.1;white-space:nowrap}
.hero-copy h2{font-size:24px;font-weight:600;letter-spacing:2px;margin-top:6px;white-space:nowrap}
.hero-copy p{font-size:14px;font-weight:600;margin-top:18px;line-height:1.6}
.hero-copy .btn{margin-top:26px}
.dots{position:absolute;left:0;right:0;bottom:26px;display:flex;justify-content:center;gap:8px}
.dots i{width:10px;height:10px;border-radius:50%;border:2px solid #fff}
.dots i:first-child{background:#fff}

/* features */
.features{height:422px;padding-top:77px}
.features .wrap{display:flex}
.feature{width:260px;text-align:center;padding:0 20px}
.feature-icon{width:50px;height:50px;border-radius:50%;background:var(--green);margin:0 auto;display:flex;align-items:center;justify-content:center}
.feature h3{font-size:14px;font-weight:700;color:var(--ink);letter-spacing:.5px;margin:22px 0 18px;white-space:nowrap}
.feature p{font-size:12.5px;line-height:1.7}
.feature p a{color:var(--green)}

/* intro band */
.intro{height:261px;background:var(--band);padding-top:50px}
.intro h2{font-size:38px;font-weight:700;color:var(--ink)}
.intro p{width:880px;font-size:12.5px;line-height:1.75;margin-top:16px}
.intro .btn{position:absolute;right:0;top:107px;padding:14px 28px}

/* section titles */
.sec-title{display:flex;align-items:center;justify-content:center;gap:34px}
.sec-title h2{font-size:24px;font-weight:700;color:var(--ink);letter-spacing:1.5px}
.arrow{width:40px;height:40px;border-radius:50%;background:var(--green);display:flex;align-items:center;justify-content:center}
.sec-sub{text-align:center;font-size:12px;color:var(--green);margin-top:6px}

/* courses */
.courses{height:699px;padding-top:94px}
.course-row{display:flex;gap:32px;margin-top:58px}
.course{width:326px;border-bottom:3px solid var(--band);background:#fff}
.course-media{height:186px}
.course h4{font-size:14px;font-weight:700;color:var(--ink);letter-spacing:1px;padding:24px 0 0 16px;line-height:1.5;min-height:82px}
.course-meta{display:flex;align-items:center;gap:12px;padding:12px 16px 22px;font-size:11px;color:var(--muted)}
.price{background:var(--teal);color:#fff;font-weight:700;font-size:11px;padding:6px 14px;border-radius:2px}

/* widgets row */
.widgets{height:455px;padding-top:20px}
.widgets .wrap{display:flex;gap:32px}
.col{width:326px}
.col h5{font-size:15px;font-weight:700;color:var(--ink);letter-spacing:1px;margin-bottom:26px}
.col h5 span{color:var(--green);font-weight:500;font-size:12px;margin-left:14px}
.news-item{display:flex;gap:14px;border-bottom:1px solid var(--line);background:var(--band);padding:14px 16px;margin-bottom:20px}
.news-thumb{width:56px;height:56px;flex:none}
.news-item h6{font-family:"Raleway",sans-serif;font-size:12px;font-weight:700;color:var(--ink);letter-spacing:1px;text-transform:uppercase}
.news-item small{font-size:11px;color:var(--muted)}
.video{height:170px;background:#111;position:relative}
.video-bar{position:absolute;left:44px;right:60px;bottom:16px;height:6px;background:#444}
.video-side{position:absolute;right:14px;top:18px;display:flex;flex-direction:column;gap:16px}
.video-side i{width:18px;height:18px;border-radius:50%;background:#ddd}
.video-cap h6{font-family:"Raleway",sans-serif;font-size:14px;font-weight:700;color:var(--ink);margin:22px 0 8px}
.video-cap p{font-size:12px;line-height:1.7}
.about-box{background:var(--band);height:365px;text-align:center;padding-top:40px}
.avatar{width:110px;height:110px;border-radius:50%;margin:0 auto;background:linear-gradient(160deg,#5b4a40,#a48670);border:4px solid #fff}
.about-box h6{font-family:"Raleway",sans-serif;color:var(--green);font-size:16px;font-weight:600;margin-top:14px}
.about-box .role{font-size:12px;color:var(--ink);font-weight:600}
.about-box p{font-size:12px;padding:12px 34px 0;line-height:1.7}
.about-box .btn{margin-top:16px;padding:10px 24px}

/* testimonials */
.testimonials{height:310px;background:var(--band);padding-top:50px}
.testimonials blockquote{width:840px;margin:46px auto 0;text-align:center;font-size:14.5px;line-height:1.8}
.testimonials cite{display:block;width:840px;margin:22px auto 0;font-style:normal;font-size:14.5px;color:var(--ink);text-align:center}
.testimonials cite span{color:var(--green)}

/* popular */
.popular{height:520px;padding-top:172px}
.popular .sec-title h2{font-size:22px}
.popular .sec-sub{color:var(--muted);margin-top:14px;font-size:12px}
.pop-row{display:flex;gap:32px;margin-top:76px}
.pop{width:326px;height:150px;position:relative;padding:44px 0 0 30px;color:#fff}
.pop h4{font-size:15px;font-weight:800;letter-spacing:1px;line-height:1.3}
.pop h4 span{font-weight:500}
.pop-1{background:linear-gradient(90deg,#6d6d6d,#b3a9a4)}
.pop-2{background:linear-gradient(90deg,#4ea9b4,#70cfd2)}
.pop-3{background:linear-gradient(90deg,#2f8cc5,#58b4e6)}

/* tweet band */
.tweet{height:227px;background:var(--green);color:#fff;text-align:center;padding-top:40px}
.tweet-ctrl{display:flex;justify-content:center;align-items:center;gap:18px}
.tweet-ctrl .arrow{background:rgba(255,255,255,.25);width:34px;height:34px}
.bird{width:40px;height:40px;border-radius:50%;background:#fff}
.tweet p{font-size:14px;font-weight:700;margin-top:26px}
.tweet small{display:block;font-size:12px;font-weight:600;margin-top:6px}

/* footer */
.site-footer{height:407px;background:var(--dark);padding-top:50px;color:#999}
.site-footer .wrap{display:flex;gap:40px}
.fcol{width:230px}
.fcol h5{font-size:13px;font-weight:700;color:#fff;letter-spacing:1px;margin-bottom:22px}
.fcol p{font-size:12.5px;line-height:1.75}
.fcourse{display:flex;gap:12px;margin-bottom:22px}
.fcourse-thumb{width:56px;height:56px;flex:none}
.fcourse p{font-size:12px;line-height:1.5;color:#bbb}
.fcourse small{font-size:11px;color:#777}
.fcourse small b{color:#999;font-weight:600}
.tags{display:flex;flex-wrap:wrap;gap:7px}
.tags span{background:var(--green);color:#fff;font-size:10px;font-weight:700;padding:5px 8px;letter-spacing:.5px}
.posts li{list-style:none;font-size:12px;padding:7px 0 7px 14px;border-bottom:1px solid #3a3a3a;position:relative}
.posts li::before{content:"";position:absolute;left:0;top:15px;width:5px;height:5px;background:#777}
.bottom-bar{height:48px;background:var(--darker);color:#777;font-size:11px}
.bottom-bar .wrap{display:flex;justify-content:space-between;align-items:center;height:48px}
</style>
</head>
<body>

<header class="site-header">
  <div class="wrap">
    <div class="brand"><span class="brand-dot"></span>tallywise</div>
    <nav class="nav"><a>HOME</a><a>WHAT WE DO?</a><a>NEWS</a><a>TESTIMONIALS</a><a>ABOUT RAY</a><a>CONTACT</a></nav>
  </div>
</header>

<section class="hero">
  <div class="hero-photo" role="img" aria-label="Photo of a student writing at a desk"></div>
  <div class="hero-copy">
    <h1>THE BEST SOLUTION</h1>
    <h2>TO CREATE AND SELL ONLINE COURSES</h2>
    <p>Praesent commodo cursus magna, vel scelerisque nisl consectetur et.<br>Maecenas sed diam eget risus varius blandit sit amet non magna.</p>
    <a class="btn btn-teal">Learn More</a>
  </div>
  <div class="dots"><i></i><i></i><i></i></div>
</section>

<section class="features">
  <div class="wrap">
    <div class="feature">
      <div class="feature-icon"><svg width="24" height="24" viewBox="0 0 24 24" fill="#fff"><circle cx="8" cy="8" r="3.5"/><circle cx="16" cy="8" r="3.5"/><path d="M2 20c0-4 3-6 6-6s6 2 6 6zM12 20c0-3 2-6 4-6 3 0 6 2 6 6z"/></svg></div>
      <h3>GROUP TUITION</h3>
      <p>tallywise Math Tuition by Ray Tan offers A levels and O levels math tuition in small groups.<br><br>Ray Tan is a specialist in JC H2 math and O levels A math tuition. To find out more about Ray, please <a>click here</a>.</p>
    </div>
    <div class="feature">
      <div class="feature-icon"><svg width="24" height="24" viewBox="0 0 24 24" fill="none" stroke="#fff" stroke-width="2"><rect x="3" y="4" width="18" height="12" rx="1"/><path d="M8 20h8M12 16v4"/></svg></div>
      <h3>BOARD-CASTS ON VIDSHELF</h3>
      <p>Whiteboard broadcast, that's what Board-cast is all about. Ray painstakingly records his lessons into Board-casts and posts them on VidShelf for all to view for free.</p>
    </div>
    <div class="feature">
      <div class="feature-icon"><svg width="24" height="24" viewBox="0 0 24 24" fill="none" stroke="#fff" stroke-width="2"><path d="M4 5h7v14H4zM13 5h7v14h-7z"/></svg></div>
      <h3>MASTERY TUTORIAL</h3>
      <p>(coming soon)<br><br>Nullam quis risus eget urna mollis ornare vel eu leo. Sed posuere consectetur est at lobortis.</p>
    </div>
    <div class="feature">
      <div class="feature-icon"><svg width="24" height="24" viewBox="0 0 24 24" fill="none" stroke="#fff" stroke-width="2"><circle cx="12" cy="12" r="8"/><path d="M12 7v5l3 3"/></svg></div>
      <h3>ULTRICIES EGESTA</h3>
      <p>Nullam quis risus eget urna mollis ornare vel eu leo. Sed posuere consectetur est at lobortis.</p>
    </div>
  </div>
</section>

<section class="intro">
  <div class="wrap">
    <h2>Maths tuition classes in Singapore</h2>
    <p>tallywise is a math tuition centre, founded by Ray Tan, who also happens to be its principal mentor. What makes us stand out from the others is our approach to teaching – which is a specialised blend of Concept and Practice (CAP). Once the concepts are in place, and their application is carried out, mastery is inevitable. It's important to have a solid foundation, as many mathematical concepts build upon each other. Students can achieve success in their scores with our reliable H2 math tuition classes, as well as relevant classes for A and O level students. Rest assured that they shall always stay one step ahead with our JC maths tuition lectures.</p>
    <a class="btn btn-dark">Learn More</a>
  </div>
</section>

<section class="courses">
  <div class="wrap">
    <div class="sec-title">
      <span class="arrow"><svg width="12" height="12" viewBox="0 0 12 12"><path d="M8 1L3 6l5 5" stroke="#fff" stroke-width="2" fill="none"/></svg></span>
      <h2>RECENT COURSES</h2>
      <span class="arrow"><svg width="12" height="12" viewBox="0 0 12 12"><path d="M4 1l5 5-5 5" stroke="#fff" stroke-width="2" fill="none"/></svg></span>
    </div>
    <div class="sec-sub">View All Courses</div>
    <div class="course-row">
      <article class="course">
        <div class="course-media" style="background:linear-gradient(135deg,#7fc8d6,#4fb0c6)" role="img" aria-label="Illustration of a rocket, light bulb and office icons"></div>
        <h4>STARTING COMPANY, ALL YOU NEED TO KNOW TO START COMPANY</h4>
        <div class="course-meta"><span class="price">$400</span>MAR 22, 2015 - MAR 26, 2015</div>
      </article>
      <article class="course">
        <div class="course-media" style="background:linear-gradient(135deg,#3a3a3a,#8a8079)" role="img" aria-label="Photo of a photographer holding a camera"></div>
        <h4>HOW TO BE A GREAT PHOTOGRAPHER</h4>
        <div class="course-meta"><span class="price">Free</span>APR 22, 2015 - APR 24, 2015</div>
      </article>
      <article class="course">
        <div class="course-media" style="background:linear-gradient(135deg,#d9cfc6,#8a5a44)" role="img" aria-label="Photo of a chef plating food in a kitchen"></div>
        <h4>HOW TO COOK LIKE FRENCH</h4>
        <div class="course-meta"><span class="price">$150</span>JUN 15, 2015 - JUN 25, 2015</div>
      </article>
    </div>
  </div>
</section>

<section class="widgets">
  <div class="wrap">
    <div class="col">
      <h5>RECENT NEWS<span>Read The Blog</span></h5>
      <div class="news-item"><div class="news-thumb" style="background:#6b5f57" role="img" aria-label="Photo thumbnail"></div><div><h6>Sem Porta Mollis Parturient</h6><small>26 Mar 2014</small></div></div>
      <div class="news-item"><div class="news-thumb" style="background:#a08f7f" role="img" aria-label="Photo thumbnail"></div><div><h6>Nullam Lorem Mattis Purus</h6><small>26 Apr 2014</small></div></div>
      <div class="news-item"><div class="news-thumb" style="background:#7a9bb0" role="img" aria-label="Photo thumbnail"></div><div><h6>Nibh Sem Sit Ullamcorper</h6><small>11 Mar 2014</small></div></div>
    </div>
    <div class="col">
      <h5>SCHOOL WALKTHROUGH</h5>
      <div class="video">
        <svg style="position:absolute;left:16px;bottom:8px" width="18" height="20" viewBox="0 0 18 20"><path d="M2 2l14 8-14 8z" fill="#fff"/></svg>
        <div class="video-bar"></div>
        <div class="video-side"><i></i><i></i><i></i></div>
      </div>
      <div class="video-cap">
        <h6>Fermentum Vulputate</h6>
        <p>Vestibulum id ligula porta felis euismod semper. Aenean eu leo quam. Pellentesque ornare sem lacinia quam venenatis vestibulum.</p>
      </div>
    </div>
    <div class="col">
      <h5>ABOUT RAY</h5>
      <div class="about-box">
        <div class="avatar" role="img" aria-label="Portrait of the tutor"></div>
        <h6>Ray Tan</h6>
        <div class="role">Maths tutor</div>
        <p>Ray Tan is a maths tutor in Singapore, who is the founding member of tallywise and is its principal tutor.</p>
        <a class="btn btn-teal">View Profile</a>
      </div>
    </div>
  </div>
</section>

<section class="testimonials">
  <div class="wrap">
    <div class="sec-title">
      <span class="arrow"><svg width="12" height="12" viewBox="0 0 12 12"><path d="M8 1L3 6l5 5" stroke="#fff" stroke-width="2" fill="none"/></svg></span>
      <h2>WHAT STUDENT SAY?</h2>
      <span class="arrow"><svg width="12" height="12" viewBox="0 0 12 12"><path d="M4 1l5 5-5 5" stroke="#fff" stroke-width="2" fill="none"/></svg></span>
    </div>
    <blockquote>Etiam porta sem malesuada magna mollis euismod. Donec id elit non mi porta gravida at eget metus. Cras mattis consectetur purus sit amet fermentum. Nulla vitae elit libero, a pharetra augue.</blockquote>
    <cite><span>Owen Marlow</span> , Programmer</cite>
  </div>
</section>

<section class="popular">
  <div class="wrap">
    <div class="sec-title"><h2>CHECK OUT SOME POPULAR COURSES</h2></div>
    <div class="sec-sub">Tellus Elit Euismod Ultricies</div>
    <div class="pop-row">
      <div class="pop pop-1" role="img" aria-label="Photo of a photographer with a camera"><h4>PHOTOGRAPHY<br><span>LESSONS</span></h4></div>
      <div class="pop pop-2" role="img" aria-label="Illustration of a rocket launch"><h4 style="padding-left:120px">ILLUSTRATION<br><span>SECRET TIPS</span></h4></div>
      <div class="pop pop-3" role="img" aria-label="Photo of hands using a phone with network icons"><h4>BOOST UP YOUR<br><span>SOCIAL MEDIA</span></h4></div>
    </div>
  </div>
</section>

<section class="tweet">
  <div class="tweet-ctrl">
    <span class="arrow"><svg width="10" height="10" viewBox="0 0 12 12"><path d="M8 1L3 6l5 5" stroke="#fff" stroke-width="2" fill="none"/></svg></span>
    <span class="bird"></span>
    <span class="arrow"><svg width="10" height="10" viewBox="0 0 12 12"><path d="M4 1l5 5-5 5" stroke="#fff" stroke-width="2" fill="none"/></svg></span>
  </div>
  <p>Check out our new theme! :-) http://lnk.to/tw8sq2</p>
  <small>146 days ago</small>
</section>

<footer class="site-footer">
  <div class="wrap">
    <div class="fcol">
      <h5>ABOUT US</h5>
      <p>Cum sociis natoque penatibus et magnis dis parturient montes, nascetur ridiculus mus. Morbi leo risus, porta ac consectetur ac, vestibulum at eros.</p>
    </div>
    <div class="fcol">
      <h5>RECENT COURSES</h5>
      <div class="fcourse"><div class="fcourse-thumb" style="background:#5aa9c0" role="img" aria-label="Course thumbnail"></div><div><p>Creative Unfold, Think outside the box</p><small>Created on <b>Aug 12, 2014</b></small></div></div>
      <div class="fcourse"><div class="fcourse-thumb" style="background:#6fc0d0" role="img" aria-label="Course thumbnail"></div><div><p>Starting Company, All you need to know to start company</p><small>Created on <b>Aug 12, 2014</b></small></div></div>
    </div>
    <div class="fcol">
      <h5>TAG CLOUD</h5>
      <div class="tags"><span>ANIMAL</span><span>BOOK</span><span>EVENT</span><span>HEALTH</span><span>MEDIA</span><span>BUSINESS</span><span>GALLERY THUMBNAIL</span><span>LIFE STYLE</span><span>LINK</span><span>NEWS</span><span>POST FORMAT</span><span>QUOTE</span><span>STANDARD</span><span>TRAVEL</span><span>VIDEO</span></div>
    </div>
    <div class="fcol">
      <h5>RECENT POSTS</h5>
      <ul class="posts"><li>Sem Porta Mollis Parturient</li><li>Nullam Lorem Mattis Purus</li><li>Nibh Sem Sit Ullamcorper</li><li>Donec luctus imperdiet</li><li>Magna pars studiorum</li><li>Sedial eiusmod tempor</li></ul>
    </div>
  </div>
</footer>
<div class="bottom-bar">
  <div class="wrap"><span>Theme By BrightPanel</span><span>Copyright © 2014 - All Right Reserved - BrightPanel Inc</span></div>
</div>

</body>
</html>
```